Business card and Stationery for data intelligence company

We need a new design for our business cards and stationery (Business Letter templates and a Quote example on Word, but it MUST work on Google Doc as well).

We are a software company based in Ireland and UK. Our product is "Quarla", data intelligence platform with beautiful visualizations, graph capabilities (things are interconnected), powerful, flexible, it can manage Big Data and Streaming information. It's modern and relatively open source.
Our company will provide data intelligence for law enforcements, pharmaceuticals, and similar high end customers.

We'll launch a new website soon. At the moment it's http://www.quarla.tech if you want to take a look. This is our youtube channel in case you need it to understand what Quarla is: https://www.youtube.com/c/quarlatechchannel

We changed the logo so please use the logo I attach here.

We'd like the output to be cool and modern but elegant and "business" at the same time. It should inspire simple sophistication, "unity" "intent" "purpose" yet subtly very advanced and innovative.

The name "Quarla" does NOT refer to sirens (mithological creatures) as well as the warning devices. It means Quantum Unified Archival Record Layer Array. Please use our logo's colors and if you want to something like the "graph" image.

```html
<!DOCTYPE html>
<html lang="en">
<head>
<meta charset="utf-8">
<title>Quarla – Business Card</title>
<link href="https://fonts.googleapis.com/css2?family=Montserrat:wght@300;500&family=Open+Sans:wght@400;600;700&display=swap" rel="stylesheet">
<style>
  :root {
    --backdrop: #d9d5cf;
    --card-light: #f3f1ec;
    --card-dark: #232323;
    --accent: #f5ab2a;
    --ink: #333333;
    --ink-soft: #555555;
    --tag-grey: #8f8f8f;
  }
  html, body {
    margin: 0;
    width: 1200px;
    height: 848px;
    overflow: hidden;
    background: var(--backdrop);
  }
  .sheet {
    position: relative;
    width: 1200px;
    height: 848px;
    display: flex;
    flex-direction: column;
    align-items: center;
    justify-content: center;
    gap: 56px;
  }
  .card {
    position: relative;
    width: 560px;
    height: 320px;
    border-radius: 18px;
    box-shadow: 0 6px 18px rgba(0,0,0,0.18);
    overflow: hidden;
  }
  /* Back: contact side */
  .card--contact {
    background: var(--card-light);
    font-family: "Open Sans", Arial, sans-serif;
    color: var(--ink);
  }
  .contact {
    position: absolute;
    left: 318px;
    top: 48px;
  }
  .contact__name {
    margin: 0;
    font-size: 24px;
    font-weight: 400;
    letter-spacing: 0.2px;
  }
  .contact__name strong { font-weight: 700; }
  .contact__role {
    margin: 2px 0 20px;
    font-size: 15px;
    font-weight: 600;
    color: var(--accent);
  }
  .contact__list {
    list-style: none;
    margin: 0;
    padding: 0;
    font-size: 15px;
    color: var(--ink-soft);
  }
  .contact__item {
    display: flex;
    align-items: flex-start;
    gap: 12px;
    margin-bottom: 9px;
    line-height: 1.3;
  }
  .contact__icon {
    flex: 0 0 14px;
    width: 14px;
    height: 14px;
    margin-top: 3px;
    fill: var(--accent);
  }
  /* Front: brand side */
  .card--brand { background: var(--card-dark); }
  .brand {
    position: absolute;
    left: 118px;
    top: 106px;
    display: flex;
    align-items: center;
    gap: 22px;
  }
  .brand__dot {
    width: 74px;
    height: 74px;
    border-radius: 50%;
    background: var(--accent);
  }
  .brand__name {
    margin: 0;
    font-family: "Montserrat", Arial, sans-serif;
    font-weight: 500;
    font-size: 46px;
    letter-spacing: 7px;
    line-height: 1;
    color: var(--accent);
  }
  .brand__tagline {
    margin: 8px 0 0 2px;
    font-family: "Montserrat", Arial, sans-serif;
    font-weight: 300;
    font-size: 13px;
    letter-spacing: 5px;
    color: var(--tag-grey);
  }
  .brand__rule {
    position: absolute;
    left: 0;
    right: 0;
    top: 262px;
    height: 3px;
    background: var(--accent);
  }
</style>
</head>
<body>
<main class="sheet">
  <section class="card card--contact">
    <div class="contact">
      <h1 class="contact__name">Jonathan <strong>Doe</strong></h1>
      <p class="contact__role">Job Title</p>
      <ul class="contact__list">
        <li class="contact__item">
          <svg class="contact__icon" viewBox="0 0 14 14"><path d="M7 0a5 5 0 0 0-5 5c0 3.6 5 9 5 9s5-5.4 5-9a5 5 0 0 0-5-5zm0 7a2 2 0 1 1 0-4 2 2 0 0 1 0 4z"/></svg>
          <span>Examplestreet Ave 63<br>12345 Sincity</span>
        </li>
        <li class="contact__item">
          <svg class="contact__icon" viewBox="0 0 14 14"><path d="M1 4c0-1.5 2.5-2.5 6-2.5S13 2.5 13 4v1.5h-3V4H4v1.5H1z"/><rect x="2" y="6.5" width="10" height="6" rx="1.2"/></svg>
          <span>000 000 0000</span>
        </li>
        <li class="contact__item">
          <svg class="contact__icon" viewBox="0 0 14 14"><path d="M0 3h14v1L7 8.5 0 4z"/><path d="M0 5.5l7 4.5 7-4.5V11H0z"/></svg>
          <span>youremail@example.com</span>
        </li>
        <li class="contact__item">
          <svg class="contact__icon" viewBox="0 0 14 14"><path d="M7 0a7 7 0 1 0 0 14A7 7 0 0 0 7 0zm0 1.5c.8 0 1.8 2 2 4.5H5c.2-2.5 1.2-4.5 2-4.5zM1.6 7.5h2c.1 1.7.4 3.1 1 4.2A5.5 5.5 0 0 1 1.6 7.5zm0-1.5A5.5 5.5 0 0 1 4.6 2.3c-.6 1.1-.9 2.2-1 3.7zm3.4 1.5h4c-.2 2.5-1.2 5-2 5s-1.8-2.5-2-5zm4.4 4.2c.6-1.1.9-2.5 1-4.2h2a5.5 5.5 0 0 1-3 4.2zm1-5.7c-.1-1.5-.4-2.6-1-3.7a5.5 5.5 0 0 1 3 3.7z"/></svg>
          <span>www.yourwebsite.com</span>
        </li>
      </ul>
    </div>
  </section>

  <section class="card card--brand">
    <div class="brand">
      <div class="brand__dot"></div>
      <div>
        <p class="brand__name">QUARLA</p>
        <p class="brand__tagline">DATA INTELLIGENCE</p>
      </div>
    </div>
    <div class="brand__rule"></div>
  </section>
</main>
</body>
</html>
```